Selka Marrow Photography Business Card

I need a new business card/ possibly design to use for other marking materials ... I have included my logo below in a few different colors, but can also provide the logo in additional colors and sizes. I would love a card the expresses clean, simple and classy.

Target Market(s)

Portrait photography clients, child photography clients

Industry/Entity Type

Photographer

Contact Information for Business Card

Selka Marrow Photography, Larkfield MA, www.selkamarrowphotography.example
T. 555-283-9146 E. selkamarrowphoto@mailbox.example

Colors
33b8a4
eea4c8
5c5c5c

Requirements
Must have
• I would like to include my logo on card.
Nice to have
• I also like the color brown as well as the choices below. I would like a simple, elegant card, something classy.

```html
<!DOCTYPE html>
<html lang="en">
<head>
<meta charset="utf-8">
<title>Selka Marrow Photography – Business Card</title>
<link rel="stylesheet" href="https://fonts.googleapis.com/css2?family=Didact+Gothic&display=swap">
<style>
  :root {
    --backdrop: #2a2b2d;
    --card-light: #ffffff;
    --card-dark: #121415;
    --teal: #4db3a8;
    --teal-bright: #7fd3c8;
  }
  * { margin: 0; padding: 0; box-sizing: border-box; }
  html, body {
    width: 1200px;
    height: 1200px;
    overflow: hidden;
    background: var(--backdrop);
    font-family: "Didact Gothic", "Century Gothic", sans-serif;
  }
  .sheet {
    width: 1200px;
    height: 1200px;
    display: flex;
    flex-direction: column;
    align-items: center;
    justify-content: center;
    gap: 60px;
  }
  .card {
    width: 840px;
    height: 480px;
    position: relative;
    display: flex;
    flex-direction: column;
    align-items: center;
    box-shadow: 0 10px 30px rgba(0,0,0,0.45);
  }
  .card--front { background: var(--card-light); color: var(--teal); }
  .card--back { background: var(--card-dark); color: var(--teal-bright); }

  .brand-name {
    position: absolute;
    top: 150px;
    left: 0;
    right: 0;
    text-align: center;
    font-size: 46px;
    letter-spacing: 0.04em;
    color: var(--teal);
  }
  .card--back .brand-name { top: 120px; color: var(--teal-bright); }

  .address {
    position: absolute;
    top: 345px;
    left: 0;
    right: 0;
    text-align: center;
    font-size: 19px;
    letter-spacing: 0.02em;
  }

  .contact {
    position: absolute;
    top: 290px;
    left: 0;
    right: 0;
    list-style: none;
    text-align: center;
    font-size: 23px;
    line-height: 1.45;
    letter-spacing: 0.02em;
  }
</style>
</head>
<body>
  <main class="sheet">
    <section class="card card--front" aria-label="Card front">
      <p class="brand-name">Selka Marrow Photography</p>
      <p class="address">Selka Marrow Photography, Larkfield MA</p>
    </section>

    <section class="card card--back" aria-label="Card back">
      <p class="brand-name">Selka Marrow Photography</p>
      <ul class="contact">
        <li class="contact__phone">555-283-9146</li>
        <li class="contact__email">selkamarrowphoto@mailbox.example</li>
        <li class="contact__web">www.selkamarrowphotography.example</li>
      </ul>
    </section>
  </main>
</body>
</html>
```